Bright Meadow Cabins Needs A Flyer

We need a flyer for our newest product "The Sunlit Garden Workpod Deluxe"

Here is some copy for the flyer:

1. More and more people everyday are working from home and finding it difficult to disconnect from home activities in order to focus on their work. They are also finding it very expensive to add on to their existing house for a quiet place. Our archatectually stunning, Sunlit Garden Workpod Deluxe is the answer. The office studio measures 16' wide and 10' deep. 160 Square feet of space.

Perfect for dozens of purposes. Home office, design studio, artist studio, home school office, reading room, craft studio, drafting room.

Features include:

- Steel Framing. 40-60% lighter then wood, higher strength to weight ratio, resistant to mold and fire and steel is the most recycled material on earth!
- Spray foam insulation. Cool in the summer and warm in the winter.
- HVAC Mini Split with wireless remote control and thermostat.
- 100% Off grid with enough solar and battery storage to run your entire office. No need to pay for an expensive electric installation.
- Flush fitting floor outlets to reduce wires.
- TV mount (Optional with pre-wired electric, HDMI, digital audio & Cat 6)
- Windows are tempered glass custom made by Vorn Glazing.
- Solar qualifies for a 26% tax credit. This is not a write-off rather it is a direct reduction on your tax obligation.
- Thousands of dollars less than adding onto your home.
- Custom color, siding, features available.

This beautiful back yard office is delivered 100% assembled and ready to enjoy on the day of delivery.

We ship nationwide from our factory in South Carolina. Give us a call anytime to speak to a designer and start your dream office today!

555-318-4720
info@BrightMeadowCabins.example

```html
<!DOCTYPE html>
<html lang="en">
<head>
<meta charset="utf-8">
<title>Bright Meadow Cabins – Sunlit Garden Workpod Deluxe Flyer</title>
<link href="https://fonts.googleapis.com/css2?family=Montserrat:wght@300;400;500;600;700;800&display=swap" rel="stylesheet">
<style>
  :root{
    --page:#eeeeec;
    --green:#55a043;
    --green-dark:#2f7d36;
    --green-text:#3c8c2e;
    --green-light:#8fd16f;
    --orange:#e8a424;
    --orange-light:#f6c25a;
    --ink:#1b1b1b;
    --white:#ffffff;
  }
  *{box-sizing:border-box;margin:0;padding:0}
  html,body{width:950px;height:1200px;overflow:hidden;background:var(--page);font-family:"Montserrat",sans-serif}
  .flyer{position:absolute;left:51px;top:0;width:848px;height:1200px;background:var(--white);overflow:hidden;box-shadow:0 0 10px rgba(0,0,0,.15)}

  /* header */
  .masthead{position:absolute;left:0;top:0;width:848px;height:163px;background:linear-gradient(#ffffff 30%,#dcdcdc)}
  .brand{position:absolute;left:95px;top:48px;width:230px;display:flex;align-items:center;gap:12px}
  .brand-dot{flex:none;width:34px;height:34px;border-radius:50%;background:var(--green)}
  .brand-name{font-weight:700;font-size:25px;line-height:1.1;color:var(--orange);letter-spacing:.3px}
  .product-title{position:absolute;left:355px;top:42px;width:475px;text-align:center;font-weight:700;font-size:33px;line-height:1.22;letter-spacing:.4px}
  .t-orange{color:var(--orange)}
  .t-green{color:var(--green-dark)}

  /* hero */
  .hero{position:absolute;left:0;top:169px;width:848px;height:260px}
  .hero svg{position:absolute;left:0;top:0}
  .hero-copy{position:absolute;left:494px;top:50px;width:335px;color:var(--white);font-size:13.6px;line-height:1.25;font-weight:400}
  .hero-copy p+p{margin-top:12px}

  /* contact + purposes band */
  .info-band{position:absolute;left:0;top:429px;width:848px;height:172px}
  .info-band svg{position:absolute;left:0;top:0}
  .contact{position:absolute;left:39px;top:12px;color:var(--white)}
  .contact-phone{font-weight:700;font-size:45px;letter-spacing:.5px}
  .contact-address{font-weight:600;font-size:19px;line-height:1.25;margin-top:4px}
  .contact-hours{font-weight:600;font-size:19px;margin-top:10px}
  .contact-hours small{font-size:15px;font-weight:500;margin-left:6px}
  .purposes{position:absolute;left:430px;top:14px;width:410px;text-align:center;color:var(--white);font-size:23.5px;line-height:1.25}
  .purposes-lead{font-size:21px;text-decoration:underline;text-underline-offset:3px;font-weight:400;margin-bottom:2px}
  .purposes b{font-weight:700}
  .p-or{color:var(--orange)}
  .p-orl{color:var(--orange-light);font-weight:300}
  .p-gr{color:var(--green-light)}
  .p-w{color:var(--white);font-weight:300}

  /* features */
  .product-views{position:absolute;left:30px;top:628px;width:262px}
  .view{display:block;background:linear-gradient(135deg,#3d3f41,#8a8378 55%,#d9d2c6)}
  .view-angle{width:250px;height:142px;margin-left:6px}
  .view-front{width:210px;height:130px;margin:57px 0 0 26px}
  .view-frame{width:262px;height:148px;margin-top:8px;background:linear-gradient(135deg,#ffffff,#9a9a9a 50%,#3e3e3e)}
  .features{position:absolute;left:316px;top:640px;width:520px;color:var(--ink)}
  .features h2{font-size:21px;font-weight:700;color:var(--green-dark);text-decoration:underline;text-underline-offset:3px;margin-bottom:12px}
  .features ul{list-style:none;font-size:13.6px;line-height:1.24}
  .features li{padding-left:9px;text-indent:-9px;margin-bottom:11px}
  .features li::before{content:"• ";}
  .features .closing{color:var(--green-text);font-size:13.6px;line-height:1.24;margin-top:16px}
  .features .closing+.closing{margin-top:11px}

  /* footer */
  .footer-bar{position:absolute;left:0;top:1145px;width:848px;height:55px}
  .footer-bar svg{position:absolute;left:0;top:0}
  .footer-tag{position:absolute;left:39px;top:11px;font-weight:800;font-size:27px;color:var(--ink)}
  .footer-contact{position:absolute;right:20px;top:17px;font-weight:600;font-size:17px;color:var(--white);white-space:nowrap}
</style>
</head>
<body>
<main class="flyer">

  <header class="masthead">
    <div class="brand">
      <span class="brand-dot"></span>
      <span class="brand-name">Bright Meadow<br>Cabins</span>
    </div>
    <h1 class="product-title">
      <span class="t-orange">THE</span> <span class="t-green">SUNLIT</span> <span class="t-orange">GARDEN</span><br>
      <span class="t-orange">WORKPOD</span> <span class="t-green">DELUXE</span>
    </h1>
  </header>

  <section class="hero">
    <svg width="848" height="260" viewBox="0 0 848 260">
      <defs>
        <linearGradient id="photoTone" x1="0" y1="0" x2="1" y2="1">
          <stop offset="0" stop-color="#d9e6e4"/>
          <stop offset=".45" stop-color="#4d5a4a"/>
          <stop offset="1" stop-color="#2f4a26"/>
        </linearGradient>
      </defs>
      <rect width="848" height="260" fill="var(--green)"/>
      <polygon points="0,0 384,0 465,150 440,260 0,260" fill="url(#photoTone)" role="img" aria-label="Photo of the dark-clad garden workpod with glass front among trees and shrubs"/>
    </svg>
    <div class="hero-copy">
      <p>More and more people everyday are working from home and finding it difficult to disconnect from home activities in order to focus on their work. They are also finding it very expensive to add on to their existing house for a quiet place.</p>
      <p>Our archatectually stunning, Sunlit Garden Workpod Deluxe is the answer. The office studio measures 16' wide and 10' deep. 160 Square feet of space.</p>
    </div>
  </section>

  <section class="info-band">
    <svg width="848" height="172" viewBox="0 0 848 172">
      <rect width="848" height="172" fill="var(--green-dark)"/>
      <polygon points="0,0 458,0 325,172 0,172" fill="var(--orange)"/>
    </svg>
    <div class="contact">
      <div class="contact-phone">555-318-4720</div>
      <div class="contact-address">2270 Larkspur Bend Rd,<br>Millbrook, SC 29000</div>
      <div class="contact-hours">8am - 4pm<small>(Monday-Saturday)</small></div>
    </div>
    <div class="purposes">
      <div class="purposes-lead">Perfect for dozens of purposes.</div>
      <b class="p-or">HOME</b> <span class="p-orl">OFFICE</span>, <span class="p-w">DESIGN</span> <b class="p-gr">STUDIO</b>,
      <span class="p-w">ARTIST</span> <b class="p-or">STUDIO</b>, <span class="p-orl">HOME</span> <b class="p-or">SCHOOL OFFICE</b>,
      <span class="p-w">READING</span> <b class="p-gr">ROOM</b>, <span class="p-w">CRAFT</span>
      <b class="p-or">STUDIO</b>, <span class="p-w">DRAFTING</span> <b class="p-gr">ROOM</b>.
    </div>
  </section>

  <div class="product-views">
    <div class="view view-angle" role="img" aria-label="Three-quarter rendering of the workpod"></div>
    <div class="view view-front" role="img" aria-label="Front elevation rendering of the workpod"></div>
    <div class="view view-frame" role="img" aria-label="Exploded steel frame diagram of the workpod"></div>
  </div>

  <section class="features">
    <h2>FEATURES INCLUDE:</h2>
    <ul>
      <li>Steel Framing. 40-60% lighter then wood, higher strength to weight ratio, resistant to mold and fire and steel is the most recycled material on earth!</li>
      <li>Spray foam insulation. Cool in the summer and warm in the winter.</li>
      <li>HVAC Mini Split with wireless remote control and thermostat.</li>
      <li>100% Off grid with enough solar and battery storage to run your entire office. No need to pay for an expensive electric installation.</li>
      <li>Flush fitting floor outlets to reduce wires.</li>
      <li>TV mount (Optional with pre-wired electric, HDMI, digital audio &amp; Cat 6)</li>
      <li>Windows are tempered glass custom made by Vorn Glazing.</li>
      <li>Solar qualifies for a 26% tax credit. This is not a write-off rather it is a direct reduction on your tax obligation.</li>
      <li>Thousands of dollars less than adding onto your home.</li>
      <li>Custom color, siding, features available.</li>
    </ul>
    <p class="closing">This beautiful back yard office is delivered 100% assembled and ready to enjoy on the day of delivery.</p>
    <p class="closing">We ship nationwide from our factory in South Carolina. Give us a call anytime to speak to a designer and start your dream office today!</p>
  </section>

  <footer class="footer-bar">
    <svg width="848" height="55" viewBox="0 0 848 55">
      <rect width="848" height="55" fill="var(--green-dark)"/>
      <polygon points="0,0 333,0 297,55 0,55" fill="var(--white)"/>
      <polygon points="0,0 320,0 284,55 0,55" fill="var(--orange)"/>
    </svg>
    <div class="footer-tag">100% OFF GRID</div>
    <div class="footer-contact">555-318-4720 | info@BrightMeadowCabins.example</div>
  </footer>

</main>
</body>
</html>
```